Coral Sleep Depot Website

Need a design for a local Miami mattress store.
The store is called Coral Sleep Depot.
need it to be something that customers can find on the internet and will
give them my location, they need to know i have the same brand mattress as the other store except i have them at almost half the price.

the office phone number is (786)555-0143
the office address is: 4127 sw Heron Bend Ave, Miami FL 33190

included is the logo, id like to stick the with white and teal design

here are is an excerpt that can or cannot be included

"We are a premium mattress discount outlet store located in South Florida; offering Free Delivery to Broward Miami-Dade, the Keys, and Palm Beach.

We carry the best brands in the market: Varnell CloudHaven; Dorvik SpineAlign, Brackett & Lowe, Pendry, among others.

We are open 7 days a week, and we are accessible from all major highways. We are a family business and our goal is to provide you with the most comfortable and best quality mattress at a price that has no competition. Come visit us and take a look at our large inventory selection."

```html
<!DOCTYPE html>
<html lang="en">
<head>
<meta charset="utf-8">
<title>Coral Sleep Depot</title>
<link rel="stylesheet" href="https://fonts.googleapis.com/css2?family=Oswald:wght@400;500&family=Open+Sans:wght@400;600&display=swap">
<style>
:root{
  --teal:#19b2c9;
  --teal-dark:#0f98ad;
  --teal-light:#4cc8da;
  --ink:#3a3a3a;
  --muted:#9a9a9a;
  --band:#efefef;
  --white:#ffffff;
  --charcoal:#333;
}
*{margin:0;padding:0;box-sizing:border-box}
html,body{width:748px;height:1200px;overflow:hidden;background:var(--white)}
body{font-family:"Open Sans",Arial,sans-serif;color:var(--ink);position:relative}
.page{position:relative;width:748px;height:1200px}

.site-header{position:absolute;top:0;left:0;width:748px;height:90px;background:linear-gradient(#fff,#f1f1f1)}
.brand{position:absolute;left:62px;top:26px;display:flex;align-items:center;gap:10px}
.brand-mark{width:22px;height:22px;background:var(--teal)}
.brand-name{font-family:"Oswald",sans-serif;font-size:26px;font-weight:400;color:var(--charcoal);letter-spacing:.5px}
.header-divider{position:absolute;left:484px;top:16px;width:1px;height:60px;background:#cfcfcf}
.header-address{position:absolute;left:516px;top:22px;font-family:"Oswald",sans-serif;font-size:18px;line-height:22px;font-weight:500;color:var(--charcoal);text-transform:uppercase}

.main-nav{position:absolute;top:90px;left:0;width:748px;height:40px;background:var(--teal);border-top:6px solid var(--teal-light)}
.main-nav ul{list-style:none;display:flex;position:absolute;left:62px;top:7px}
.main-nav li{font-size:10px;color:var(--white);text-transform:uppercase;margin-right:26px;letter-spacing:.3px}
.main-nav li.current{border-bottom:1px solid var(--white)}
.search{position:absolute;left:505px;top:6px;width:165px;height:20px;display:flex}
.search-field{flex:1;background:var(--white);font-size:9px;color:#aaa;padding:4px 6px}
.search-button{width:26px;background:var(--charcoal);display:flex;align-items:center;justify-content:center}

.hero{position:absolute;top:133px;left:0;width:748px;height:282px}
.hero-photo{position:absolute;inset:0;background:linear-gradient(180deg,#8d8f93 0%,#c9c9cb 40%,#efefef 65%,#d7d9db 100%)}
.hero-arrow{position:absolute;top:120px;width:28px;height:50px;background:var(--teal);display:flex;align-items:center;justify-content:center}
.hero-arrow.prev{left:68px}
.hero-arrow.next{right:68px}
.hero-caption{position:absolute;left:0;bottom:0;width:748px;height:70px;background:rgba(25,178,201,.75);text-align:center;color:var(--white)}
.hero-title{font-family:"Oswald",sans-serif;font-size:29px;font-weight:400;margin-top:6px;text-transform:uppercase}
.hero-sub{font-size:10px}

.tagline{position:absolute;top:415px;left:0;width:748px;height:90px;background:var(--band);text-align:center;padding-top:20px}
.tagline p{font-family:"Oswald",sans-serif;font-size:20px;line-height:25px;color:var(--charcoal);text-transform:uppercase}
.tagline em{font-style:normal;color:var(--teal)}

.brands{position:absolute;top:505px;left:0;width:748px;height:240px}
.brand-card{position:absolute;top:27px;width:140px;height:188px;background:#f2f2f2;padding:5px 5px 0}
.brand-photo{height:148px}
.brand-label{position:absolute;left:0;bottom:0;width:100%;height:32px;background:var(--teal);color:var(--white);font-family:"Oswald",sans-serif;font-size:14px;text-transform:uppercase;display:flex;align-items:center;justify-content:center}

.partners{position:absolute;top:745px;left:0;width:748px;height:170px;background:var(--band)}
.partners h2{font-family:"Oswald",sans-serif;font-weight:400;font-size:20px;color:var(--teal);text-align:center;margin-top:18px;text-transform:uppercase}
.partner-badge{position:absolute;top:57px;width:88px;height:88px;background:var(--white);border:1px solid #ddd;display:flex;align-items:center;justify-content:center}
.partner-badge span{width:62px;height:62px;background:#d3d6da;border-radius:8px}
.carousel-dot{position:absolute;top:90px;width:22px;height:22px;border-radius:50%;background:var(--white);border:2px solid var(--teal);display:flex;align-items:center;justify-content:center}

.info{position:absolute;top:915px;left:0;width:748px;height:190px}
.info h3{font-family:"Oswald",sans-serif;font-weight:400;font-size:15px;color:var(--teal);text-transform:uppercase;margin-bottom:8px}
.info-col{position:absolute;top:22px;font-size:9.5px;line-height:14px;color:var(--muted)}
.hours{left:74px;width:120px}
.hours li{list-style:none;line-height:18px}
.about{left:212px;width:222px}
.about a,.visit a{color:var(--teal);text-decoration:none}
.visit{left:478px;width:205px}
.visit .label{color:var(--ink)}

.site-footer{position:absolute;top:1105px;left:0;width:748px;height:95px;background:var(--teal);text-align:center;color:var(--white)}
.contact-icons{display:flex;justify-content:center;gap:8px;margin-top:12px}
.contact-icons span{width:26px;height:26px;border-radius:50%;background:var(--white);display:flex;align-items:center;justify-content:center}
.footer-links{font-size:10px;margin-top:12px}
.copyright{font-size:9px;margin-top:3px}
</style>
</head>
<body>
<div class="page">

  <header class="site-header">
    <div class="brand"><span class="brand-mark"></span><span class="brand-name">Coral Sleep Depot</span></div>
    <div class="header-divider"></div>
    <div class="header-address">4127 sw Heron Bend Ave,<br>Miami FL 33190</div>
  </header>

  <nav class="main-nav">
    <ul>
      <li class="current">Home</li>
      <li>We are mattress discounters</li>
      <li>Location</li>
      <li>Get in touch.</li>
    </ul>
    <div class="search">
      <div class="search-field">Search</div>
      <div class="search-button">
        <svg width="11" height="11" viewBox="0 0 11 11"><circle cx="4.5" cy="4.5" r="3.3" fill="none" stroke="#fff" stroke-width="1.5"/><line x1="7" y1="7" x2="10" y2="10" stroke="#fff" stroke-width="1.5"/></svg>
      </div>
    </div>
  </nav>

  <section class="hero">
    <div class="hero-photo" role="img" aria-label="Photo of a plush white mattress with pillows in a bedroom"></div>
    <div class="hero-arrow prev"><svg width="12" height="26" viewBox="0 0 12 26"><polyline points="10,2 2,13 10,24" fill="none" stroke="#fff" stroke-width="2"/></svg></div>
    <div class="hero-arrow next"><svg width="12" height="26" viewBox="0 0 12 26"><polyline points="2,2 10,13 2,24" fill="none" stroke="#fff" stroke-width="2"/></svg></div>
    <div class="hero-caption">
      <div class="hero-title">Mattress to fit any room</div>
      <div class="hero-sub">The same brands as the big stores, at almost half the price.</div>
    </div>
  </section>

  <section class="tagline">
    <p>We have <em>mattresses on sale</em> of all shapes and sizes. <em>Ultimate</em></p>
    <p>solutions for your sleeping needs.</p>
  </section>

  <section class="brands">
    <div class="brand-card" style="left:62px"><div class="brand-photo" role="img" aria-label="Photo of a dark-framed mattress set" style="background:linear-gradient(#2f2f31,#e6e6e6 55%,#3a3a3a)"></div><div class="brand-label">Varnell CloudHaven</div></div>
    <div class="brand-card" style="left:222px"><div class="brand-photo" role="img" aria-label="Photo of a mattress in a grey bedroom" style="background:linear-gradient(#4a4a4c,#dcdcdc 55%,#9a9a9a)"></div><div class="brand-label">Dorvik SpineAlign</div></div>
    <div class="brand-card" style="left:381px"><div class="brand-photo" role="img" aria-label="Photo of a family sitting on a mattress" style="background:linear-gradient(#cfc7bd,#b9a89a 50%,#e8e8e8)"></div><div class="brand-label">Brackett &amp; Lowe</div></div>
    <div class="brand-card" style="left:540px"><div class="brand-photo" role="img" aria-label="Photo of a quilted mattress with pillows" style="background:linear-gradient(#6b6660,#eeeeee 55%,#bdbdbd)"></div><div class="brand-label">Pendry</div></div>
  </section>

  <section class="partners">
    <h2>Our partners</h2>
    <div class="carousel-dot" style="left:62px"><svg width="8" height="10" viewBox="0 0 8 10"><polygon points="7,0 0,5 7,10" fill="#19b2c9"/></svg></div>
    <div class="partner-badge" style="left:118px"><span></span></div>
    <div class="partner-badge" style="left:223px"><span></span></div>
    <div class="partner-badge" style="left:328px"><span></span></div>
    <div class="partner-badge" style="left:433px"><span></span></div>
    <div class="partner-badge" style="left:538px"><span></span></div>
    <div class="carousel-dot" style="left:662px"><svg width="8" height="10" viewBox="0 0 8 10"><polygon points="1,0 8,5 1,10" fill="#19b2c9"/></svg></div>
  </section>

  <section class="info">
    <div class="info-col hours">
      <h3>Store hours</h3>
      <ul>
        <li>Mon: 9am-7pm</li><li>Tue: 9am-7pm</li><li>Wed: 9am-7pm</li><li>Thu: 9am-7pm</li><li>Fri: 9am-7pm</li><li>Sat: 9am-7pm</li><li>Sun: 9am-7pm</li>
      </ul>
    </div>
    <div class="info-col about">
      <h3>Coral Sleep Depot</h3>
      <p>Coral Sleep Depot was founded in 2014, but our beginning started in 2000 with small classified ads offering customers home delivery of mattresses. We've come a long way since those modest beginnings. Over the years our name is synonymous with the most competitive prices with impeccable service and delivery of a good night's sleep.</p>
      <a href="#">Read More</a>
    </div>
    <div class="info-col visit">
      <h3>Visit us</h3>
      <p>Feel free to contact us and find out how we can help you find your perfect mattress.</p>
      <p style="margin-top:8px"><span class="label">Phone:</span> <a href="#">(786)555-0143</a></p>
      <p><span class="label">Email:</span> <a href="#">hello@coralsleepdepot.com</a></p>
      <p class="label">North Miami:</p>
      <p><a href="#">208 NW 171 St, FL 33169</a></p>
      <p class="label" style="margin-top:6px">South Miami:</p>
      <p><a href="#">4127 SW Heron Bend Ave #55, FL 33190</a></p>
    </div>
  </section>

  <footer class="site-footer">
    <div class="contact-icons">
      <span aria-label="Phone"><svg width="14" height="14" viewBox="0 0 14 14"><path d="M3 1.5l2 2.5-1.2 1.5c.8 1.7 2 2.9 3.7 3.7L9 8l2.5 2-1 2.2C6 12 2 8 1.8 3.5z" fill="#19b2c9"/></svg></span>
      <span aria-label="Location"><svg width="12" height="14" viewBox="0 0 12 14"><path d="M6 13.5S1.5 8.5 1.5 5.2a4.5 4.5 0 0 1 9 0C10.5 8.5 6 13.5 6 13.5z" fill="#19b2c9"/><circle cx="6" cy="5.2" r="1.7" fill="#fff"/></svg></span>
      <span aria-label="Email"><svg width="14" height="10" viewBox="0 0 14 10"><rect x="0.5" y="0.5" width="13" height="9" fill="#19b2c9"/><polyline points="0.5,0.5 7,5.5 13.5,0.5" fill="none" stroke="#fff" stroke-width="1.2"/></svg></span>
    </div>
    <div class="footer-links">We are mattress discounters &nbsp;/&nbsp; Location &nbsp;/&nbsp; Get in Touch.</div>
    <div class="copyright">Copyright © 2014 Coral Sleep Depot. All rights reserved.</div>
  </footer>

</div>
</body>
</html>
```